'Wedding Business" Business Card Design

dj services for weddings and parties, uplighting, event planning, day of coordination for weddings, photography for weddings and other events.

Would like raised print and metallic also if possible. Elegant design, yet modern. This is a wedding business and should describe our goals and main services - DJ/lighting, wedding and event planning, photography. slogan "Simply Incredible, Incredibly simple" or "Your Dreams. Our Experience. The Perfect Match" Our goal is to provide multiple services to make it easier for the bride and groom almost like a one stop shop. Feel free to use the slogan or leave it out , we just want to really stand out against the competition. You can also get more info on our website www.bluelarkproductions.com - we are working to get the bluelarkct.com site pointed to our current site!

there should be 2 files attached, if they did not go through please email events@bluelarkct.com or bluelarkproductions@mailbox.test
Updates

Thank you all for your help, we have decided what we like but would like to make some changes, we need to order these asap so please let us know if you can help.

Reason: Wasn't able to pick it out in time! So Sorry but we know what we want!!

Industry/Entity Type

Business

Contact Information for Business Card

Trevor and Mallory Quenby
555-318-2746
555-207-4831
Blue Lark Productions, Events, & Photography
EMAIL:Events@BlueLarkCT.com
www.bluelarkct.com

```html
<!DOCTYPE html>
<html lang="en">
<head>
<meta charset="utf-8">
<title>Blue Lark Productions — Business Card</title>
<link rel="stylesheet" href="https://fonts.googleapis.com/css2?family=Open+Sans:wght@400;600;700&display=swap">
<style>
  :root {
    --page: #e9e6e1;
    --card-black: #050505;
    --royal-blue: #3a4aa6;
    --swoosh-white: #ffffff;
    --text-white: #ffffff;
    --text-soft: #e4e4e4;
    --logo-silver: #cdd2db;
    --gem-blue: #2c3fb0;
    --card-shadow: rgba(0,0,0,0.28);
  }
  * { box-sizing: border-box; margin: 0; padding: 0; }
  html, body {
    width: 1200px; height: 900px; overflow: hidden;
    background: var(--page);
    font-family: "Open Sans", Arial, sans-serif;
  }
  .canvas {
    position: relative; width: 1200px; height: 900px;
  }
  .card {
    position: absolute; left: 250px; width: 700px; height: 400px;
    background: var(--card-black);
    box-shadow: 0 10px 28px var(--card-shadow);
    overflow: hidden;
  }
  .card--back { top: 40px; }
  .card--front { top: 460px; }

  .card__art { position: absolute; inset: 0; width: 100%; height: 100%; }

  .brand {
    position: absolute; display: flex; align-items: center; gap: 12px;
    color: var(--logo-silver); font-weight: 600; white-space: nowrap;
  }
  .brand__gem {
    width: 18px; height: 18px; border-radius: 50%; background: var(--gem-blue);
    flex: none;
  }
  .card--back .brand { left: 0; right: 0; top: 170px; justify-content: center; font-size: 44px; }
  .card--back .brand__gem { width: 22px; height: 22px; }
  .card--front .brand { left: 200px; top: 172px; font-size: 40px; }

  .contact {
    position: absolute; right: 32px; top: 74px; text-align: right;
    color: var(--text-white);
  }
  .contact__name { font-size: 25px; font-weight: 700; line-height: 1.1; }
  .contact__role { font-size: 14px; color: var(--text-soft); margin-bottom: 20px; }
  .contact__address { font-size: 14.5px; line-height: 1.4; color: var(--text-soft); margin-bottom: 18px; }
  .contact__lines { list-style: none; font-size: 15.5px; line-height: 1.38; }
  .contact__lines li { display: flex; justify-content: flex-end; align-items: center; gap: 9px; }
  .contact__icon { width: 12px; height: 12px; flex: none; fill: var(--text-white); }
</style>
</head>
<body>
<main class="canvas">

  <section class="card card--back" aria-label="Business card back">
    <div class="brand"><span class="brand__gem"></span>Blue Lark</div>
  </section>

  <section class="card card--front" aria-label="Business card front">
    <svg class="card__art" viewBox="0 0 700 400" aria-hidden="true">
      <rect width="700" height="400" fill="var(--royal-blue)"/>
      <path d="M150,0 L700,0 L700,362 L470,400 L165,400 C50,320 45,120 150,0 Z" fill="var(--card-black)"/>
      <path d="M160,0 C62,110 66,300 168,400 L186,400 C106,300 100,110 186,0 Z" fill="var(--swoosh-white)"/>
    </svg>

    <div class="brand"><span class="brand__gem"></span>Blue Lark</div>

    <div class="contact">
      <p class="contact__name">Trevor Quenby</p>
      <p class="contact__role">Managing Partner</p>
      <p class="contact__address">2210 Harbor Lane,<br>Mystic, CT 06355</p>
      <ul class="contact__lines">
        <li>(555) 318-2746
          <svg class="contact__icon" viewBox="0 0 12 12"><path d="M2.5 1l2 2.2-1 1.3c.8 1.6 1.8 2.6 3.4 3.4l1.3-1 2.2 2-1.4 1.6C5 10.5 1.5 7 .9 2.4z"/></svg>
        </li>
        <li>(555) 318-2747
          <svg class="contact__icon" viewBox="0 0 12 12"><path d="M3 1h5v3H3zM1 5h10v5H9V8H3v2H1zM3 9h6v2H3z"/></svg>
        </li>
        <li>(555) 207-4831
          <svg class="contact__icon" viewBox="0 0 12 12"><path d="M3 0h6v12H3zM4 1.5v8h4v-8z"/></svg>
        </li>
        <li>trevor@bluelarkct.com
          <svg class="contact__icon" viewBox="0 0 12 12"><path d="M0 2h12v8H0zM1 3l5 3.5L11 3z" fill-rule="evenodd"/></svg>
        </li>
        <li>www.bluelarkct.com
          <svg class="contact__icon" viewBox="0 0 12 12"><circle cx="6" cy="6" r="5.2" fill="none" stroke="#fff" stroke-width="1.2"/><path d="M1 6h10M6 .8c-2.4 3-2.4 7.4 0 10.4M6 .8c2.4 3 2.4 7.4 0 10.4" fill="none" stroke="#fff" stroke-width="1"/></svg>
        </li>
      </ul>
    </div>
  </section>

</main>
</body>
</html>
```